依頼概要
■依頼の目的/概要
弊社の経営理念を作成しましたが、社内掲示用にポスターの作成をお願いします。

■依頼詳細
ミッション・ビジョン・バリューをポスター1枚に収めてください。
HPにも掲載できればと考えています。

■重視する点
掲載内容は添付ファイルをご確認ください。

過去の提案(同業者なので)を見て応募しようと考えました。
https://www.pitchora.jp/work/detail/4731852

■弊社の紹介
東京都内で廃棄物を収集・処分する会社です。詳しくは下記Official HPをご覧ください。
https://www.miyakura-k.co.jp

HP検討挿入予定個所
https://www.miyakura-k.co.jp/company

■その他
掲載内容の文言はあまり整理されていないのでうまい具合にご調整ください。

■その他ご不明点はお気軽にお問合せください。

発注時のイメージ通りの作品だったため。

この度は、沢山のご応募ありがとうございます。
皆さんのご提案が多く、選定に迷いました。

また機会がございましたら、よろしくお願いします。

```html
<!DOCTYPE html>
<html lang="ja">
<head>
<meta charset="utf-8">
<title>経営理念 Mission Vision Value</title>
<link rel="stylesheet" href="https://fonts.googleapis.com/css2?family=Jost:wght@400;500&family=Noto+Sans+JP:wght@400;500&display=swap">
<style>
  :root {
    --sky-top: #2f98c6;
    --sky-mid: #7cc7c0;
    --leaf: #a9d8a2;
    --mist: #eef5ef;
    --ink: #333a3d;
  }
  * { margin: 0; padding: 0; box-sizing: border-box; }
  html, body { width: 861px; height: 1200px; overflow: hidden; }
  body {
    font-family: "Noto Sans JP", sans-serif;
    color: var(--ink);
    background: var(--mist);
  }
  .poster {
    position: relative;
    width: 861px;
    height: 1200px;
    overflow: hidden;
  }
  .backdrop {
    position: absolute;
    inset: 0;
    background:
      radial-gradient(ellipse 70% 40% at 50% 62%, rgba(255,255,255,0.85), rgba(255,255,255,0) 70%),
      linear-gradient(180deg, var(--sky-top) 0%, var(--sky-mid) 22%, var(--leaf) 40%, #cfe8cc 58%, var(--mist) 82%, #f7faf7 100%);
  }
  .principle {
    position: absolute;
    left: 0;
    width: 100%;
    text-align: center;
  }
  .principle--mission { top: 120px; }
  .principle--vision { top: 410px; }
  .principle--value { top: 738px; }
  .label {
    position: relative;
    display: inline-block;
    font-size: 20px;
    font-weight: 500;
    letter-spacing: 0.08em;
    padding: 0 26px;
  }
  .label::before,
  .label::after {
    content: "";
    position: absolute;
    top: 50%;
    width: 18px;
    height: 1.5px;
    background: var(--ink);
  }
  .label::before { left: 0; transform: rotate(55deg); }
  .label::after { right: 0; transform: rotate(-55deg); }
  .heading {
    font-family: "Jost", sans-serif;
    font-weight: 500;
    font-size: 62px;
    letter-spacing: 0.14em;
    line-height: 1;
    margin-top: 12px;
  }
  .statement {
    margin-top: 46px;
    font-size: 20px;
    line-height: 40px;
    letter-spacing: 0.12em;
  }
  .brand {
    position: absolute;
    right: 36px;
    bottom: 50px;
    font-size: 18px;
    font-weight: 500;
    letter-spacing: 0.1em;
    color: var(--ink);
  }
</style>
</head>
<body>
<main class="poster">
  <div class="backdrop" role="img" aria-label="青い空から緑へ移る背景に、白く淡い木々のシルエットが広がるイラスト"></div>

  <section class="principle principle--mission">
    <p class="label">社会的使命</p>
    <h2 class="heading">Mission</h2>
    <p class="statement">
      地球環境を保全するために<br>
      静脈産業を支える社会インフラの役割を全うし<br>
      すべての人に快適でクリーンな世界を提供する
    </p>
  </section>

  <section class="principle principle--vision">
    <p class="label">中長期計画</p>
    <h2 class="heading">Vision</h2>
    <p class="statement">
      先進的 (Advansed) な取り組みを行い<br>
      廃棄物業界リード (Lead) し<br>
      高品質 (High quolity) なサービスを提供し<br>
      働きがいがある会社づくりを行う
    </p>
  </section>

  <section class="principle principle--value">
    <p class="label">大切な価値観</p>
    <h2 class="heading">Value</h2>
    <p class="statement">
      活発なコミュニケーションの元情報共有を行い<br>
      チームワークに溢れる組織風土の中で協働し<br>
      何事にも真摯に向き合い正直な気持ちで<br>
      チャレンジ行動力を持って自己実現を目指す
    </p>
  </section>

  <p class="brand">宮倉環境株式会社</p>
</main>
</body>
</html>
```